Vantel Solutions Website Design

We are a B2B startup offering a free virtual data room and deal management platform for small businesses. We need a 10-page website geared towards business executives and entrepreneurs that is simple, uploads quickly and provides a good introduction to our product. We've attached a document setting forth the text of 8 of the 10 pages (the other two - Resources and Blog - need to be designed to allow the future posting of white papers and blog entries) and links to the screenshots and GIFs, all of which are in a folder on filewell. We've also attached a zip file with our logo and a pdf file with our font and colors. Examples of websites we like include www.marbletoft.example, www.usepivra.example and https://kelmo.example.

Target Market(s)

Small business owners, business executives and entrepreneurs

Industry/Entity Type

Finance

Coding

Number of Pages Required

5+ page

Font styles to use
Sans Serif

Colors
85abd2
f9ba93

Requirements
Must have
• Please use the Wordpress harbor theme I uploaded to code the site.
Nice to have
• Clean, uncluttered design. White background. Screenshots and gifs should be shown on monitors (desktop, laptop and iPad only). Blue and orange are our corporate colors, but you’re not limited to those two colors. See uploaded logo guide for complementary colors or use your own judgment.

```html
<!DOCTYPE html>
<html lang="en">
<head>
<meta charset="utf-8">
<title>Vantel Solutions</title>
<link href="https://fonts.googleapis.com/css2?family=Roboto:wght@300;400;500&display=swap" rel="stylesheet">
<style>
:root{
  --blue:#85abd2;
  --blue-text:#4d7aa6;
  --orange:#e8720c;
  --orange-soft:#f9ba93;
  --slate:#4b7189;
  --slate-btn:#4e7592;
  --ink:#4a4a4a;
  --muted:#6a6a6a;
  --grey-bg:#f3f3f3;
  --line:#d8d8d8;
  --white:#ffffff;
}
*{box-sizing:border-box;margin:0;padding:0}
html,body{width:1200px;height:3493px;overflow:hidden;background:var(--white)}
body{font-family:"Roboto",Arial,sans-serif;color:var(--ink);position:relative}
section,header,footer{position:absolute;left:0;width:1200px}
.abs{position:absolute}

/* header */
.site-header{top:0;height:70px;border-top:4px solid var(--orange-soft);background:var(--white);z-index:3}
.brand{left:86px;top:16px;font-size:32px;font-weight:500;color:var(--slate)}
.nav{top:30px;font-size:13px;color:var(--slate);white-space:nowrap}
.nav.active{color:var(--orange)}
.btn{display:flex;align-items:center;justify-content:center;border-radius:20px;letter-spacing:.5px;white-space:nowrap}
.nav-cta{left:920px;top:24px;width:256px;height:32px;background:var(--slate-btn);color:var(--white);font-size:14px}
.dropdown{left:641px;top:56px;width:96px;background:var(--white);border:1px solid #e4e4e4;padding:3px 0;font-size:11px;line-height:13px;color:var(--orange);white-space:nowrap}
.dropdown div{padding:3px 8px;border-bottom:1px solid #eee}
.dropdown div:first-child{color:var(--slate)}
.dropdown div:last-child{border-bottom:0;color:var(--ink)}

/* hero */
.hero{top:70px;height:465px}
.hero-copy{left:84px;top:44px;width:420px}
.hero-copy h1{font-size:34px;font-weight:300;line-height:42px;color:var(--ink)}
.hero-copy h1 span{color:var(--blue-text)}
.hero-copy .intro{margin-top:22px;width:310px;font-size:12.5px;line-height:17px}
.hero-copy ul{margin-top:22px;padding-left:20px;font-size:12.5px;line-height:17px;color:var(--blue-text)}
.hero-copy .outro{margin-top:16px;width:410px;font-size:12.5px;line-height:17px}
.demo-btn{margin-top:20px;width:198px;height:34px;border:1.5px solid var(--slate);color:var(--slate);font-size:15px}
.laptop{left:570px;top:46px;width:606px;height:338px;border-radius:14px 14px 4px 4px;background:linear-gradient(180deg,#2c2f33 0,#44484e 72%,#c9ccd0 73%,#8f9398 100%)}

/* features */
.features{top:535px;height:641px;background:var(--blue);color:var(--white);text-align:center}
.features h2{position:absolute;left:0;width:1200px;top:18px;font-size:31px;font-weight:300}
.features .sub{position:absolute;left:0;width:1200px;top:70px;font-size:14px;color:#e8f0f8}
.feature{position:absolute;width:260px}
.feature svg{display:block;margin:0 auto}
.feature h3{font-size:17px;font-weight:400;margin-top:10px}
.feature p{font-size:12.5px;line-height:18px;color:#e1ebf6;margin:6px auto 0;width:190px}

/* quote */
.quote{top:1183px;height:172px;background:var(--grey-bg);text-align:center}
.quote blockquote{position:absolute;left:0;width:1200px;top:38px;font-size:21px;font-weight:300;line-height:28px;color:var(--ink)}
.quote cite{position:absolute;left:0;width:1200px;top:100px;font-size:11px;font-style:normal;color:var(--muted)}
.quote .rule{left:84px;top:119px;width:1031px;height:32px;border:1px solid var(--line);background:var(--white)}

/* product blocks */
.block-title{font-size:32px;font-weight:300;color:var(--ink);width:440px;white-space:nowrap}
.block-title::after{content:"";display:block;width:250px;height:2px;background:var(--orange-soft);margin-top:10px}
.block-title.right{text-align:right}
.block-title.right::after{margin-left:auto}
.block-text{font-size:12.5px;line-height:19px;color:var(--muted);width:260px}
.block-text.right{text-align:right}
.screen{border:4px solid #1d1f22;border-top-width:10px;border-bottom-width:10px;background:linear-gradient(90deg,#dfe4ea 0,#f6f7f9 30%,#ffffff 100%)}

/* cta */
.cta{top:2881px;height:217px;background:var(--orange);text-align:center;color:var(--white)}
.cta h2{position:absolute;left:0;width:1200px;top:48px;font-size:30px;font-weight:300}
.cta p{position:absolute;left:0;width:1200px;top:92px;font-size:15px;color:#fde3cf}
.cta .btn{left:450px;top:123px;width:300px;height:42px;background:var(--slate-btn);font-size:20px}

/* footer */
.site-footer{top:3098px;height:356px;background:var(--slate);color:var(--white)}
.footer-brand{left:156px;top:62px;font-size:38px;font-weight:500}
.divider{top:30px;width:1px;height:300px;background:#6f8fa3}
.footer-head{font-size:12px;font-weight:500;letter-spacing:.5px}
.contacts{left:156px;top:190px;font-size:11px;line-height:18px;color:#dfe8ee}
.contacts .row{display:flex;align-items:flex-start;gap:8px}
.contacts svg{margin-top:3px;flex:none}
.links{left:501px;top:92px;width:198px;font-size:12px;color:#dfe8ee}
.links div{height:39px;padding-top:8px;border-bottom:1px solid #6f8fa3}
.social{left:845px;top:102px;width:194px;font-size:11px;line-height:14px;color:#dfe8ee}
.social .item{display:flex;align-items:center;gap:12px;height:56px;border-bottom:1px solid #6f8fa3}
.social .dot{width:28px;height:28px;border-radius:50%;background:var(--white);flex:none}
.social .dot.on{background:var(--orange)}
.bottom-bar{top:3454px;height:39px;background:var(--orange);color:var(--white);font-size:12px;display:flex;align-items:center;justify-content:center}
</style>
</head>
<body>

<header class="site-header">
  <div class="abs brand">Vantel</div>
  <div class="abs nav" style="left:494px">Home</div>
  <div class="abs nav" style="left:560px">Features</div>
  <div class="abs nav active" style="left:641px">Our Clients</div>
  <div class="abs nav" style="left:740px">Company</div>
  <div class="abs nav" style="left:829px">Contact Us</div>
  <div class="abs btn nav-cta">TRY IT NOW BUTTON</div>
  <div class="abs dropdown">
    <div>Finance</div><div>Insurance</div><div>Real Estate</div><div>Small Business</div>
  </div>
</header>

<section class="hero">
  <div class="abs hero-copy">
    <h1>Manage Your Workflow<br>Better with <span>Vantel</span></h1>
    <p class="intro">The Vantel Assistant is a secure, sharable workflow management platform designed with your needs in mind. Here are some features you'll love:</p>
    <ul>
      <li>Built for internal and external collaboration</li>
      <li>Highly customizable and intuitive</li>
      <li>Free to use – no setup or monthly fees</li>
    </ul>
    <p class="outro">If you want to process contracts faster while reducing costs (did we mention that it was free?), <b style="font-weight:500">Vantel</b> is the ideal solution for you.</p>
    <div class="btn demo-btn">WATCH DEMO</div>
  </div>
  <div class="abs laptop" role="img" aria-label="Laptop showing the Vantel workflow dashboard"></div>
</section>

<section class="features">
  <h2>Features At-a-Glance</h2>
  <div class="sub">User-friendly workflow management software that saves time and money</div>
  <div class="feature" style="left:110px;top:130px">
    <svg width="54" height="52" viewBox="0 0 54 52"><polygon points="27,2 34,19 52,19 38,31 43,49 27,38 11,49 16,31 2,19 20,19" fill="none" stroke="#fff" stroke-width="2.5" stroke-linejoin="round"/></svg>
    <h3>Workflow Management</h3>
    <p>Efficiently handle multi-party transactions with customizable, collaborative workflow software.</p>
  </div>
  <div class="feature" style="left:471px;top:130px">
    <svg width="54" height="52" viewBox="0 0 54 52"><polygon points="27,2 34,19 52,19 38,31 43,49 27,38 11,49 16,31 2,19 20,19" fill="none" stroke="#fff" stroke-width="2.5" stroke-linejoin="round"/></svg>
    <h3>Workflow Management</h3>
    <p>Efficiently handle multi-party transactions with customizable, collaborative workflow software.</p>
  </div>
  <div class="feature" style="left:827px;top:130px">
    <svg width="54" height="52" viewBox="0 0 54 52"><polygon points="27,2 34,19 52,19 38,31 43,49 27,38 11,49 16,31 2,19 20,19" fill="none" stroke="#fff" stroke-width="2.5" stroke-linejoin="round"/></svg>
    <h3>Workflow Management</h3>
    <p>Efficiently handle multi-party transactions with customizable, collaborative workflow software.</p>
  </div>
  <div class="feature" style="left:110px;top:370px">
    <svg width="54" height="52" viewBox="0 0 54 52"><polygon points="27,2 34,19 52,19 38,31 43,49 27,38 11,49 16,31 2,19 20,19" fill="none" stroke="#fff" stroke-width="2.5" stroke-linejoin="round"/></svg>
    <h3>Workflow Management</h3>
    <p>Efficiently handle multi-party transactions with customizable, collaborative workflow software.</p>
  </div>
  <div class="feature" style="left:471px;top:370px">
    <svg width="54" height="52" viewBox="0 0 54 52"><polygon points="27,2 34,19 52,19 38,31 43,49 27,38 11,49 16,31 2,19 20,19" fill="none" stroke="#fff" stroke-width="2.5" stroke-linejoin="round"/></svg>
    <h3>Workflow Management</h3>
    <p>Efficiently handle multi-party transactions with customizable, collaborative workflow software.</p>
  </div>
  <div class="feature" style="left:827px;top:370px">
    <svg width="54" height="52" viewBox="0 0 54 52"><polygon points="27,2 34,19 52,19 38,31 43,49 27,38 11,49 16,31 2,19 20,19" fill="none" stroke="#fff" stroke-width="2.5" stroke-linejoin="round"/></svg>
    <h3>Workflow Management</h3>
    <p>Efficiently handle multi-party transactions with customizable, collaborative workflow software.</p>
  </div>
</section>

<section class="quote">
  <blockquote>“Efficient workflow management has resulted in an 85% savings<br>in deal closings over the past six years.”</blockquote>
  <cite>– The Global Council for Contract Operations –</cite>
  <div class="abs rule"></div>
</section>

<div class="abs block-title" style="left:84px;top:1490px">Waste Less, Do More</div>
<p class="abs block-text" style="left:84px;top:1560px">Reduce administrative costs by streamlining workflows and automating document storage and sharing from a single, cloud-based platform.</p>
<div class="abs screen" style="left:650px;top:1444px;width:465px;height:238px" role="img" aria-label="Screenshot of the Vantel document dashboard"></div>

<div class="abs screen" style="left:114px;top:1805px;width:436px;height:249px" role="img" aria-label="Screenshot of the Vantel task list view"></div>
<div class="abs block-title right" style="left:675px;top:1858px">Waste Less, Do More</div>
<p class="abs block-text right" style="left:855px;top:1925px">Reduce administrative costs by streamlining workflows and automating document storage and sharing from a single, cloud-based platform.</p>

<div class="abs block-title" style="left:84px;top:2210px">Waste Less, Do More</div>
<p class="abs block-text" style="left:84px;top:2280px">Reduce administrative costs by streamlining workflows and automating document storage and sharing from a single, cloud-based platform.</p>
<div class="abs screen" style="left:650px;top:2161px;width:465px;height:238px" role="img" aria-label="Screenshot of the Vantel document dashboard"></div>

<div class="abs screen" style="left:114px;top:2527px;width:436px;height:244px" role="img" aria-label="Screenshot of the Vantel task list view"></div>
<div class="abs block-title right" style="left:675px;top:2578px">Waste Less, Do More</div>
<p class="abs block-text right" style="left:855px;top:2645px">Reduce administrative costs by streamlining workflows and automating document storage and sharing from a single, cloud-based platform.</p>

<section class="cta">
  <h2>Manage Your Workflow with Vantel</h2>
  <p>Try it today. You'll wonder how you got by without it.</p>
  <div class="abs btn">TRY IT NOW BUTTON</div>
</section>

<footer class="site-footer">
  <div class="abs footer-brand">Vantel</div>
  <div class="abs contacts">
    <div class="footer-head" style="margin-bottom:8px">OUR CONTACTS:</div>
    <div class="row"><svg width="10" height="13" viewBox="0 0 10 13"><path d="M5 0C2.2 0 0 2.2 0 5c0 3.5 5 8 5 8s5-4.5 5-8c0-2.8-2.2-5-5-5z" fill="#f9ba93"/><circle cx="5" cy="5" r="1.8" fill="#4b7189"/></svg><span>1122, Any City, Any Street<br>Any Country, 14256</span></div>
    <div class="row"><svg width="11" height="11" viewBox="0 0 11 11"><path d="M2 0l2 2.5-1.2 1.5c.8 1.6 2.2 3 3.7 3.7L8 6.5 11 8.5 9.5 11C4.5 10.5.5 6.5 0 1.5z" fill="#f9ba93"/></svg><span>+00 - 5550102030</span></div>
    <div class="row"><svg width="12" height="9" viewBox="0 0 12 9"><rect width="12" height="9" rx="1" fill="#f9ba93"/><path d="M0 0l6 5 6-5" fill="none" stroke="#4b7189"/></svg><span>contact@vantelsolutions.example</span></div>
  </div>
  <div class="abs divider" style="left:426px"></div>
  <div class="abs divider" style="left:769px"></div>
  <div class="abs footer-head" style="left:501px;top:56px">USEFUL LINKS</div>
  <div class="abs links">
    <div>› Home</div><div>› Products</div><div>› Resources</div><div>› Downloads</div><div>› Career</div><div>› Contact Us</div>
  </div>
  <div class="abs footer-head" style="left:845px;top:56px">SOCIAL LINKS</div>
  <div class="abs social">
    <div class="item"><span class="dot"></span><span>Like us<br>on Friendloop</span></div>
    <div class="item"><span class="dot on"></span><span>Follow us<br>on Chirpwell</span></div>
    <div class="item"><span class="dot"></span><span>Follow us<br>on Circlehub</span></div>
    <div class="item"><span class="dot"></span><span>Follow us<br>on Workweave</span></div>
  </div>
</footer>

<div class="abs bottom-bar" style="left:0;width:1200px">Copyrights © 2014 All Rights Reserved &nbsp;|&nbsp; Terms of Use / Privacy Policy</div>

</body>
</html>
```